Personal Business Card

Looking for a clean and modern personal business card. Basically I need something catchy to give to potential clients and people I meet. I do a lot of freelancing (from DJ'ing to wedding videography, but its mostly on the event side of things) so it's more-so about selling myself rather than identifying with a company. I'm starting to meet more people that I want to work with after meeting them so I'm revamping my business cards.

I'm looking for a clean and modern design- I know that's really vague but I'm fine with anything ranging from a symbol to just a fancy version of my name.

Details I need on the front:
Dennis Kowal
dennis@denniskowal-mail.net
(555) 807-2291

On the back I'd like to have something simple like "Nice to have met you today" or "Great meeting you".

UPDATE 9/27 Noon: My apologies for not putting it up before- I'm definitely looking for full color. Doesn't have to be a rainbow but I am looking for the least amount of blank white as possible.

UPDATE 10/1: Really impressed with what I've been getting so far and I'm working on giving everyone feedback- if your design is still up then you're still in the run. Looking for something more unique and modern so please do not post something that looks like a template from Cardloom!

Target Market(s)

Mainly to give to people aged 18-35. Most of my encounters will be casual so the card should have a "young" feeling to it. I rarely do anything in the corporate world so it doesn't have to be boring. It should give the impression that I'm the one they should go to if they need what I do (again it changes every weekend so I'll probably say the "what I do" part.

Industry/Entity Type

Wedding

Requirements
Must have
• Basically the contact information listed above
Nice to have
• I really like the colors Blue, Silver, and Purple. They don't have to necessarily all be there though. I do like the look of polished metal if that makes sense.
Should not have
• A template that resembles card-loom. I'm in a point in my life where I'm working a lot of different markets/areas so the card does not need to have an address or address placeholder.

```html
<!DOCTYPE html>
<html lang="en">
<head>
<meta charset="utf-8">
<title>Dennis Kowal — Business Card</title>
<link rel="stylesheet" href="https://fonts.googleapis.com/css2?family=Almendra:wght@700&family=PT+Sans:wght@700&family=Varela+Round&display=swap">
<style>
  :root {
    --page: #ffffff;
    --gold-light: #f4e6a2;
    --gold-pale: #f4e8bd;
    --gold-mid: #b59c6f;
    --gold-dark: #7a5a2e;
    --gold-edge: #e6d49c;
    --frame-dark: #3b2a10;
    --ink-brown: #4a3512;
    --plate-black: #050505;
    --paper: #ececec;
    --orange: #f07d3a;
    --orange-soft: #eea05a;
    --yellow: #f7d93a;
    --violet: #3a2d86;
    --white: #ffffff;
  }
  * { margin: 0; padding: 0; box-sizing: border-box; }
  html, body {
    width: 1083px; height: 1200px; overflow: hidden; background: var(--page);
  }
  .canvas { position: relative; width: 1083px; height: 1200px; }

  .card {
    position: absolute; left: 81px; width: 920px; height: 495px;
    border: 3px solid var(--gold-edge);
    overflow: hidden;
  }

  /* Front */
  .card-front {
    top: 71px;
    background: linear-gradient(180deg, var(--gold-light) 0%, var(--gold-pale) 38%, var(--gold-mid) 62%, var(--gold-dark) 100%);
    box-shadow: inset 3px 0 0 var(--frame-dark), inset -3px 0 0 var(--frame-dark);
  }
  .name-plate {
    position: absolute; left: 29px; top: 208px; width: 302px; height: 89px;
    background: var(--plate-black);
    border: 2px solid var(--gold-edge);
    box-shadow: inset 0 0 0 2px #2a2a2a;
    display: flex; align-items: center; justify-content: center;
  }
  .name {
    font-family: "Varela Round", sans-serif;
    font-size: 37px; color: var(--white); letter-spacing: 0.5px;
  }
  .contact-frame {
    position: absolute; left: 462px; top: 154px; width: 332px; height: 197px;
    background: linear-gradient(180deg, #e8cf7d, #a8843f 55%, #d9bd6e);
    border: 2px solid #c8ad6a;
    box-shadow: 0 1px 2px rgba(0,0,0,0.35);
  }
  .contact-panel {
    position: absolute; left: 13px; top: 11px; right: 12px; bottom: 11px;
    background: var(--paper);
    box-shadow: inset 0 0 6px rgba(0,0,0,0.35);
  }
  .contact-line {
    position: absolute; left: 30px; display: flex; align-items: center; gap: 22px;
    font-family: "PT Sans", sans-serif; font-weight: 700;
    font-size: 15.5px; color: var(--ink-brown);
  }
  .contact-line svg { width: 20px; height: 20px; fill: var(--ink-brown); }
  .contact-phone { top: 40px; }
  .contact-email { top: 97px; }

  /* Back */
  .card-back { top: 631px; height: 497px; }
  .dot-field {
    position: absolute; inset: 0;
    background: linear-gradient(180deg, var(--orange) 0%, var(--orange-soft) 20%, var(--yellow) 38%, var(--yellow) 62%, var(--orange-soft) 82%, var(--orange) 100%);
  }
  .greeting-band {
    position: absolute; left: 0; right: 0; top: 188px; height: 111px;
    background:
      linear-gradient(90deg, rgba(247,217,58,0.85) 0%, rgba(200,190,200,0.5) 4%, rgba(58,45,134,0) 9%, rgba(58,45,134,0) 91%, rgba(200,190,200,0.5) 96%, rgba(247,217,58,0.85) 100%),
      var(--violet);
    display: flex; align-items: center; justify-content: center;
  }
  .greeting {
    font-family: "Almendra", serif; font-weight: 700;
    font-size: 41px; color: var(--white);
  }
</style>
</head>
<body>
<main class="canvas">
  <section class="card card-front">
    <div class="name-plate"><h1 class="name">Dennis Kowal</h1></div>
    <div class="contact-frame">
      <div class="contact-panel">
        <p class="contact-line contact-phone">
          <svg viewBox="0 0 24 24" aria-hidden="true"><path d="M6.6 10.8a15.1 15.1 0 0 0 6.6 6.6l2.2-2.2a1 1 0 0 1 1-.25 11.4 11.4 0 0 0 3.6.57 1 1 0 0 1 1 1V20a1 1 0 0 1-1 1A17 17 0 0 1 3 4a1 1 0 0 1 1-1h3.5a1 1 0 0 1 1 1c0 1.25.2 2.45.57 3.57a1 1 0 0 1-.25 1z"/></svg>
          <span>(555) 807-2291</span>
        </p>
        <p class="contact-line contact-email">
          <svg viewBox="0 0 24 24" aria-hidden="true"><path d="M2 5h20v14H2z" fill="none"/><path d="M2 5h20v2l-10 6L2 7z"/><path d="M2 9l10 6 10-6v10H2z"/></svg>
          <span>dennis@denniskowal-mail.net</span>
        </p>
      </div>
    </div>
  </section>

  <section class="card card-back">
    <div class="dot-field" role="img" aria-label="Dotted pattern fading from orange to yellow"></div>
    <div class="greeting-band"><p class="greeting">Nice to have met you today</p></div>
  </section>
</main>
</body>
</html>
```